Consulting Company needs business card design

We need a business card design for a new consulting and business solutions company based in Bermuda called Corvale Partners Limited. Looking for a double sided business card with one side only including the company logo thats attached and the other including contact information. Logo contains blue and turquoise colors and is fine to be on both sides of the card.
Contact Information for Business Card
Corvale Partners Limited
P.O. Box HM318
Ashcombe AS 04
Bermuda
Name: Marcus Pellegrin
Position: Director
Telephone: 1 441 733 4906
Email: mpellegrin@corvale.example
Website: www.corvale.example

```html
<!DOCTYPE html>
<html lang="en">
<head>
<meta charset="utf-8">
<title>Corvale Partners Limited – Business Card</title>
<link rel="stylesheet" href="https://fonts.googleapis.com/css2?family=Roboto:wght@400;500;700&display=swap">
<style>
  :root {
    --canvas-bg: #2b2b2d;
    --card-dark: #1b1b1d;
    --card-light: #ffffff;
    --brand-blue: #1aa0dc;
    --ink: #1a1a1a;
    --font-main: "Roboto", Arial, sans-serif;
  }
  * { box-sizing: border-box; margin: 0; padding: 0; }
  html, body {
    width: 1200px;
    height: 997px;
    overflow: hidden;
    background: var(--canvas-bg);
    font-family: var(--font-main);
  }
  .canvas { position: relative; width: 1200px; height: 997px; }
  .card {
    position: absolute;
    left: 220px;
    width: 760px;
    height: 434px;
    border-radius: 22px;
    overflow: hidden;
  }
  .card--back {
    top: 43px;
    background: var(--card-dark);
    display: flex;
    align-items: center;
    justify-content: center;
  }
  .card--front { top: 520px; background: var(--card-light); }
  .brand-name {
    color: var(--brand-blue);
    font-weight: 500;
    text-transform: uppercase;
    letter-spacing: 0.06em;
    line-height: 1.05;
  }
  .card--back .brand-name { font-size: 58px; text-align: center; }
  .card--back .brand-name span { display: block; font-size: 30px; letter-spacing: 0.18em; margin-top: 8px; }
  .front-brand {
    position: absolute;
    top: 120px;
    right: 52px;
    display: flex;
    align-items: center;
    gap: 14px;
  }
  .front-brand .brand-mark { width: 58px; height: 58px; border-radius: 50%; background: var(--brand-blue); }
  .front-brand .brand-name { font-size: 30px; }
  .front-brand .brand-name span { display: block; font-size: 16px; letter-spacing: 0.16em; margin-top: 3px; }
  .accent-bar {
    position: absolute;
    left: 0;
    top: 72px;
    width: 14px;
    height: 36px;
    background: var(--brand-blue);
  }
  .contact { position: absolute; left: 56px; top: 62px; color: var(--ink); }
  .person-name { color: var(--brand-blue); font-weight: 700; font-size: 22px; letter-spacing: 0.02em; }
  .person-role { font-size: 15px; margin-top: 3px; }
  .address { margin-top: 48px; font-size: 18px; line-height: 1.2; font-style: normal; }
  .address .company { color: var(--brand-blue); font-weight: 700; font-size: 19px; }
  .reach { margin-top: 44px; list-style: none; font-size: 18px; }
  .reach li { display: flex; align-items: center; gap: 12px; line-height: 1.5; }
  .reach svg { width: 16px; height: 16px; fill: var(--brand-blue); flex: none; }
  .reach .web { color: var(--brand-blue); font-weight: 700; }
</style>
</head>
<body>
<main class="canvas">
  <section class="card card--back" aria-label="Card back">
    <div class="brand-name">Corvale<span>Partners Limited</span></div>
  </section>

  <section class="card card--front" aria-label="Card front">
    <div class="accent-bar"></div>
    <div class="contact">
      <h1 class="person-name">MARCUS PELLEGRIN</h1>
      <p class="person-role">Director</p>
      <address class="address">
        <div class="company">Corvale Partners Limited</div>
        <div>P.O. Box HM318, Ashcombe</div>
        <div>AS 04, Bermuda</div>
      </address>
      <ul class="reach">
        <li>
          <svg viewBox="0 0 16 16" aria-hidden="true"><path d="M3.5 1.5l2.6 0 1.2 3.3-1.7 1.2c.8 1.7 2.2 3.1 3.9 3.9l1.2-1.7 3.3 1.2v2.6c0 .8-.7 1.5-1.5 1.5C7 13.5 2 8.5 2 3c0-.8.7-1.5 1.5-1.5z"/></svg>
          <span>1 441 733 4906</span>
        </li>
        <li>
          <svg viewBox="0 0 16 16" aria-hidden="true"><path d="M1 3h14v10H1z M1.6 3.6L8 8.6l6.4-5" stroke="#fff" stroke-width="1.2"/></svg>
          <span>mpellegrin@corvale.example</span>
        </li>
        <li>
          <svg viewBox="0 0 16 16" aria-hidden="true"><circle cx="8" cy="8" r="7"/><path d="M1 8h14M8 1c-3 3.5-3 10.5 0 14M8 1c3 3.5 3 10.5 0 14" stroke="#fff" stroke-width="1" fill="none"/></svg>
          <span class="web">www.corvale.example</span>
        </li>
      </ul>
    </div>
    <div class="front-brand">
      <div class="brand-mark"></div>
      <div class="brand-name">Corvale<span>Partners Limited</span></div>
    </div>
  </section>
</main>
</body>
</html>
```